Produktetikett für Mikronährstoffe
Wir sind sehr zufrieden und schätzen die schnelle Umsetzung von Änderungswünschen. Herzlichen Dank an Wilmaru
Zielgruppe
Herstellung und Vertrieb von Desinfektionsmitteln und jetz neu Mikronährstoffe. Und darum geht es. Wir möchten ein Etikett gestalten lassen das modern ist und trotzdem unsere Firmenfarben und unser Logo (evtl. stilisiert) enthält. Wahrscheinlich werden wir eine braune Flasche (ähnl. Apothekerflaschen) wählen.
Aufgabenstellung
Produktetikett für Mikronährstoffe (im Nahrungsergänzungsbereich) Die Ausführung der Flasche ist noch nicht bekannnt, jedoch schwebt uns eine braune oder dunkelgrüne Flasche vor. Auch gibt es noch keinen Namen für das Produkt.

```html
<!DOCTYPE html>
<html lang="de">
<head>
<meta charset="utf-8">
<title>Produktetikett Mikronährstoffkonzentrat</title>
<link href="https://fonts.googleapis.com/css2?family=Nunito:wght@400;600;800&display=swap" rel="stylesheet">
<style>
  :root {
    --bg: #d8d3ce;
    --label: #f4f3ef;
    --frame: #b9d46e;
    --leaf-green: #8cb83c;
    --teal: #1f8ea8;
    --badge-green: #4e9a3a;
    --white: #ffffff;
  }
  * { margin: 0; padding: 0; box-sizing: border-box; }
  html, body { width: 1129px; height: 1200px; overflow: hidden; }
  body {
    background: var(--bg);
    font-family: "Nunito", sans-serif;
    position: relative;
  }
  .label {
    position: absolute;
    left: 164px; top: 100px;
    width: 800px; height: 1000px;
    background: var(--label);
    overflow: hidden;
    box-shadow: 0 10px 30px rgba(0,0,0,0.12);
  }
  .label-frame {
    position: absolute; inset: 14px;
    border: 3px solid var(--frame);
    z-index: 5;
    pointer-events: none;
  }
  .brand {
    position: absolute;
    top: 100px; left: 0; right: 0;
    text-align: center;
    font-size: 54px;
    font-weight: 600;
    letter-spacing: 1px;
    color: var(--teal);
  }
  .product-name {
    position: absolute;
    top: 235px; left: 0; right: 0;
    text-align: center;
    font-size: 60px;
    font-weight: 600;
    color: var(--teal);
  }
  .produce-illustration {
    position: absolute;
    left: 110px; top: 420px;
    width: 580px; height: 240px;
    border-radius: 50% 50% 40% 40% / 60% 60% 40% 40%;
    background: radial-gradient(ellipse at 50% 55%, #e9a23b 0%, #a8c64a 45%, #d7673b 70%, rgba(244,243,239,0) 78%);
  }
  .badge {
    position: absolute;
    left: 610px; top: 590px;
    width: 150px; height: 150px;
    border: 3px solid var(--badge-green);
    border-radius: 50%;
    background: var(--label);
    color: var(--badge-green);
    text-align: center;
    font-weight: 800;
    z-index: 3;
    padding-top: 24px;
    line-height: 1.05;
  }
  .badge-count { font-size: 46px; }
  .badge-count small { font-size: 20px; vertical-align: middle; margin-right: 4px; }
  .badge-text { font-size: 19px; font-weight: 600; }
  .green-band {
    position: absolute;
    left: 0; bottom: 0;
    width: 800px; height: 340px;
  }
  .band-content {
    position: absolute;
    left: 60px; right: 60px; top: 765px;
    text-align: center;
    color: var(--white);
    z-index: 2;
  }
  .product-type {
    font-size: 34px;
    font-weight: 800;
    letter-spacing: 0.5px;
    margin-bottom: 12px;
  }
  .product-description {
    font-size: 23px;
    font-weight: 400;
    line-height: 1.3;
  }
</style>
</head>
<body>
  <main class="label">
    <div class="label-frame"></div>

    <div class="brand">VITALORA</div>

    <h1 class="product-name">Frisch in den Morgen</h1>

    <div class="produce-illustration" role="img" aria-label="Illustration aus Obst: Mango, Äpfel, Birne, Kiwi, Orange, Banane, Erdbeeren und Pflaume"></div>

    <div class="badge">
      <div class="badge-count"><small>Mit</small>70</div>
      <div class="badge-text">Natürlichen<br>Zutaten</div>
    </div>

    <svg class="green-band" viewBox="0 0 800 340" preserveAspectRatio="none" aria-hidden="true">
      <path d="M0 150 C 150 20, 450 0, 800 40 L800 340 L0 340 Z" fill="var(--leaf-green)"/>
      <path d="M300 340 C 480 300, 650 250, 800 180 L800 215 C 660 280, 520 320, 420 340 Z" fill="var(--label)" opacity="0.9"/>
    </svg>

    <div class="band-content">
      <h2 class="product-type">MIKRONÄHRSTOFFKONZENTRAT</h2>
      <p class="product-description">Aus Obst, Gemüse, Kräutern und<br>pflanzlichen Ölen – ergänzt mit wertvollen<br>Vitaminen und Spurenelementen auf<br>wissenschaftlicher Basis.</p>
    </div>
  </main>
</body>
</html>
```